Poetry Book Cover Design Project

Looking for a minimalistic book cover design for a collection of poems. The book title is "Where The Lanterns Drift Slowly Apart". There are three parts to the book. First covers poetry in the theme of Rage. Second love and desire. The third is strange poems. Essentially the sections are "Rage", "Desire" and the "Strange". The reason for the title "Where The Lanterns Drift Slowly Apart" is as if someone is writing these till life changes towards the intended outcome as felt in each poem. I want to have the author's name "Nuwanthi Karunasekera" at the bottom. Ilustration attached.
- Minimalistic

```html
<!DOCTYPE html>
<html lang="en">
<head>
<meta charset="utf-8">
<title>Where The Lanterns Drift Slowly Apart</title>
<link rel="stylesheet" href="https://fonts.googleapis.com/css2?family=Cinzel:wght@400&family=Cormorant+Garamond:wght@500&display=swap">
<style>
  :root {
    --silver-deep: #b9babc;
    --silver-mid: #c7c8ca;
    --silver-light: #e6e6e7;
    --sheen: #fbfbfb;
    --ink: #111111;
  }
  html, body {
    margin: 0;
    padding: 0;
    width: 840px;
    height: 1200px;
    overflow: hidden;
  }
  .cover {
    position: relative;
    width: 840px;
    height: 1200px;
    overflow: hidden;
    background:
      radial-gradient(ellipse 260px 520px at 78% 46%, rgba(255,255,255,0.55), rgba(255,255,255,0) 70%),
      linear-gradient(128deg,
        var(--silver-mid) 0%,
        var(--silver-deep) 22%,
        var(--silver-mid) 40%,
        var(--silver-light) 52%,
        var(--sheen) 62%,
        var(--silver-light) 74%,
        var(--silver-mid) 86%,
        var(--silver-deep) 100%);
  }
  .cover__title {
    position: absolute;
    top: 236px;
    left: 16px;
    right: 0;
    margin: 0;
    text-align: center;
    font-family: "Cinzel", "Trajan Pro", serif;
    font-weight: 400;
    font-size: 58px;
    line-height: 62.5px;
    color: var(--ink);
    letter-spacing: 0.01em;
  }
  .cover__title span {
    display: block;
  }
  .cover__author {
    position: absolute;
    top: 1100px;
    left: 12px;
    right: 0;
    margin: 0;
    text-align: center;
    font-family: "Cormorant Garamond", "Garamond", serif;
    font-weight: 500;
    font-size: 25px;
    color: var(--ink);
    letter-spacing: 0.01em;
  }
</style>
</head>
<body>
  <main class="cover">
    <h1 class="cover__title">
      <span>Where</span>
      <span>The</span>
      <span>Lanterns</span>
      <span>Drift</span>
      <span>Slowly</span>
      <span>Apart</span>
    </h1>
    <p class="cover__author">Nuwanthi Karunasekera</p>
  </main>
</body>
</html>
```